Medical Waste Company with Logo

Need a business card design that targets office managers in the medical community. This card will be the front line for our sales team to market our services to the community. We would like to have email, phone number, website. Please use the logo attached to create a design that we would be proud of.

Target Market(s)

Medical Clients

Industry/Entity Type

Medical Supply

Contact Information for Business Card

Please use logo attached

Colors

Designer to choose colors to be used in the design.

Requirements
Must have
• Our logo (see attached file)
Nice to have
• Maybe a pop of some sort, raised..?

```html
<!DOCTYPE html>
<html lang="en">
<head>
<meta charset="utf-8">
<title>Northpeak Clinical – Business Card</title>
<link rel="stylesheet" href="https://fonts.googleapis.com/css2?family=Montserrat:wght@400;600;700&family=Roboto:wght@300;400&display=swap">
<style>
  :root {
    --bg: #1c1c1e;
    --card-white: #f7f7f7;
    --brand-blue: #0f64a6;
    --brand-blue-deep: #054a7c;
    --back-top: #1370b0;
    --back-bottom: #05497b;
    --back-mark: #0a5a94;
    --ink-grey: #6b6b6b;
    --divider: #d4d4d4;
  }
  html, body {
    margin: 0;
    padding: 0;
    width: 1200px;
    height: 974px;
    overflow: hidden;
    background: var(--bg);
  }
  .stage {
    width: 1200px;
    height: 974px;
    display: flex;
    flex-direction: column;
    align-items: center;
    justify-content: center;
    gap: 56px;
  }
  .card {
    width: 700px;
    height: 400px;
    box-sizing: border-box;
    position: relative;
  }
  /* Front */
  .card-front {
    background: var(--card-white);
    display: flex;
    align-items: center;
  }
  .brand-block {
    width: 370px;
    display: flex;
    flex-direction: column;
    align-items: center;
    justify-content: center;
    gap: 14px;
  }
  .brand-row {
    display: flex;
    align-items: center;
    gap: 12px;
  }
  .brand-square {
    width: 22px;
    height: 22px;
    background: var(--brand-blue);
  }
  .brand-name {
    font-family: "Montserrat", sans-serif;
    font-weight: 700;
    font-size: 30px;
    letter-spacing: 1px;
    color: var(--brand-blue);
    text-transform: uppercase;
    margin: 0;
  }
  .brand-rule {
    width: 260px;
    height: 2px;
    background: var(--brand-blue);
  }
  .divider {
    width: 1px;
    height: 200px;
    background: var(--divider);
  }
  .contact-block {
    padding-left: 40px;
    font-family: "Roboto", sans-serif;
    color: var(--ink-grey);
  }
  .person-name {
    font-family: "Montserrat", sans-serif;
    font-weight: 700;
    font-size: 21px;
    color: var(--brand-blue);
    text-transform: uppercase;
    margin: 0;
  }
  .person-title {
    font-size: 16px;
    font-weight: 300;
    margin: 2px 0 16px;
  }
  .contact-list {
    list-style: none;
    margin: 0 0 10px;
    padding: 0;
  }
  .contact-list li {
    display: flex;
    align-items: center;
    gap: 10px;
    font-size: 16px;
    line-height: 25px;
  }
  .contact-list svg {
    width: 14px;
    height: 14px;
    flex: none;
  }
  .address {
    font-size: 16px;
    line-height: 22px;
    margin: 0;
  }
  /* Back */
  .card-back {
    background: linear-gradient(180deg, var(--back-top) 0%, var(--back-bottom) 100%);
    display: flex;
    flex-direction: column;
    align-items: center;
    justify-content: center;
    gap: 14px;
  }
  .card-back .brand-name {
    color: var(--back-mark);
    font-size: 34px;
  }
  .card-back .brand-square { background: var(--back-mark); }
  .card-back .brand-rule { background: var(--back-mark); width: 300px; }
</style>
</head>
<body>
<main class="stage">
  <section class="card card-front">
    <div class="brand-block">
      <div class="brand-row">
        <span class="brand-square"></span>
        <p class="brand-name">Northpeak Clinical</p>
      </div>
      <div class="brand-rule"></div>
    </div>
    <div class="divider"></div>
    <div class="contact-block">
      <h1 class="person-name">Jordan Ellery</h1>
      <p class="person-title">General Manager</p>
      <ul class="contact-list">
        <li>
          <svg viewBox="0 0 24 24" aria-hidden="true"><path fill="#0f64a6" d="M6.6 10.8a15 15 0 0 0 6.6 6.6l2.2-2.2c.3-.3.7-.4 1-.2 1.1.4 2.3.6 3.6.6.6 0 1 .4 1 1V20c0 .6-.4 1-1 1A17 17 0 0 1 3 4c0-.6.4-1 1-1h3.5c.6 0 1 .4 1 1 0 1.3.2 2.5.6 3.6.1.3 0 .7-.2 1z"/></svg>
          555-318-2047
        </li>
        <li>
          <svg viewBox="0 0 24 24" aria-hidden="true"><rect x="2" y="5" width="20" height="14" fill="#0f64a6"/><path d="M2 5l10 8 10-8" fill="none" stroke="#f7f7f7" stroke-width="1.6"/></svg>
          hello@northpeakclinical.com
        </li>
        <li>
          <svg viewBox="0 0 24 24" aria-hidden="true"><g fill="none" stroke="#0f64a6" stroke-width="1.8"><circle cx="12" cy="12" r="9.5"/><ellipse cx="12" cy="12" rx="4" ry="9.5"/><path d="M2.5 12h19M4 7h16M4 17h16"/></g></svg>
          www.northpeakclinical.com
        </li>
      </ul>
      <p class="address">402 Cedar Ridge<br>Rd. Franklin, TN 37064</p>
    </div>
  </section>

  <section class="card card-back">
    <div class="brand-row">
      <span class="brand-square"></span>
      <p class="brand-name">Northpeak Clinical</p>
    </div>
    <div class="brand-rule"></div>
  </section>
</main>
</body>
</html>
```